Asphalt Paving Specialists Business Cards

Our company is KORVEN ASPHALT. We need a business cards two of our asphalt paving team members. We're asphalt specialists.
I need two made up please. The details on the front of the each business card i would like please is as follows.
Address is 87 Tindale Ave, Clontarf, QLD, 4019.

Company Director
Gregory Pellinham
greg@korven-example.com.au
04 87 659 042
www.korven-example.com.au

Supervisor
Lewis Marchetti
lewis@korven-example.com.au
0468 701 385
www.korven-example.com.au

We do all aspects of Asphalt Paving. Specific Services include - Driveways, Carparks & sub-divisions. All Roads. Repairs and Maintenance.

We provide free quotes!

I dont have a certain way i want them to look so im open to all designs :)

** I have uploaded our logo for the KORVEN ASPHALT. HOWEVER, CAN YOU PLEASE GET RID OF THE ( PTY LTD )

Thank you
Carina Holt
KORVEN ASPHALT

Target Market(s)

Home owners and Business Owners

Contact Information for Business Card

Asphalt Paving Specialists. All aspects of Asphalt. Residential, Commercial & Industrial. Based in Brisbane.

Font styles to use
Sans Serif

Colors

Designer to choose colors to be used in the design.

Requirements
Nice to have
• maybe an image of a driveway? or Asphalt?

```html
<!DOCTYPE html>
<html lang="en">
<head>
<meta charset="utf-8">
<title>Korven Asphalt – Business Card</title>
<link rel="stylesheet" href="https://fonts.googleapis.com/css2?family=Lato:wght@400;700;900&family=Alegreya:ital,wght@1,700&display=swap">
<style>
  :root {
    --backdrop: #6a3f22;
    --kraft-light: #d2b080;
    --kraft-mid: #bd9766;
    --kraft-dark: #a9855a;
    --ink: #161310;
    --rule: #2a221a;
  }
  * { margin: 0; padding: 0; box-sizing: border-box; }
  html, body {
    width: 1200px;
    height: 900px;
    overflow: hidden;
    background: var(--backdrop);
  }
  .canvas {
    position: relative;
    width: 1200px;
    height: 900px;
  }
  .card {
    position: absolute;
    left: 330px;
    width: 556px;
    height: 343px;
    background: radial-gradient(ellipse at 50% 0%, var(--kraft-light) 0%, var(--kraft-mid) 55%, var(--kraft-dark) 100%);
    color: var(--ink);
    font-family: "Lato", sans-serif;
    text-align: center;
    box-shadow: 2px 3px 6px rgba(0,0,0,0.45);
  }
  .card--front { top: 90px; }
  .card--back { top: 470px; }

  .contact {
    position: absolute;
    top: 90px;
    left: 0;
    right: 0;
  }
  .contact__name {
    font-size: 20px;
    font-weight: 700;
    letter-spacing: 0.2px;
    line-height: 24px;
  }
  .contact__role {
    font-size: 15px;
    line-height: 17px;
  }
  .contact__rule {
    width: 157px;
    height: 1px;
    margin: 10px auto 9px;
    background: var(--rule);
  }
  .contact__line {
    font-size: 16px;
    line-height: 20px;
  }
  .contact__label { font-weight: 700; }
  .contact__address {
    font-size: 15.5px;
    line-height: 20px;
  }

  .brand {
    position: absolute;
    top: 112px;
    left: 0;
    right: 0;
    display: flex;
    align-items: center;
    justify-content: center;
    gap: 14px;
  }
  .brand__mark {
    width: 40px;
    height: 40px;
    background: var(--ink);
  }
  .brand__name {
    font-size: 36px;
    font-weight: 900;
    letter-spacing: 1px;
    color: var(--ink);
  }
  .services {
    position: absolute;
    top: 205px;
    left: 0;
    right: 0;
  }
  .services__tagline {
    font-family: "Alegreya", serif;
    font-style: italic;
    font-weight: 700;
    font-size: 20px;
    line-height: 26px;
    margin-bottom: 6px;
  }
  .services__list {
    font-size: 15px;
    line-height: 21px;
  }
  .services__offer {
    margin-top: 12px;
    font-size: 15px;
    font-weight: 700;
  }
</style>
</head>
<body>
<main class="canvas">
  <section class="card card--front" aria-label="Business card front">
    <div class="contact">
      <p class="contact__name">GREGORY PELLINHAM</p>
      <p class="contact__role">Company Director</p>
      <div class="contact__rule"></div>
      <p class="contact__line"><span class="contact__label">P:</span> 04 87 659 042</p>
      <p class="contact__line"><span class="contact__label">E:</span> greg@korven-example.com.au</p>
      <p class="contact__line"><span class="contact__label">W:</span> www.korven-example.com.au</p>
      <div class="contact__rule"></div>
      <p class="contact__address">87 Tindale Ave, Clontarf, QLD, 4019</p>
    </div>
  </section>

  <section class="card card--back" aria-label="Business card back">
    <div class="brand">
      <span class="brand__mark" aria-hidden="true"></span>
      <span class="brand__name">KORVEN ASPHALT</span>
    </div>
    <div class="services">
      <p class="services__tagline">We do all aspects of Asphalt Paving.</p>
      <p class="services__list">Specific Services include - Driveways, Carparks &amp; sub-divisions.<br>All Roads. Repairs and Maintenance.</p>
      <p class="services__offer">WE PROVIDE FREE QUOTES!</p>
    </div>
  </section>
</main>
</body>
</html>
```